Tri-Fold Brochure for Christian Author and Speaker

Lorena Watkiss is an inspirational author and speaker, sharing her testimony and encouraging others in their walk with Christ. A gifted writer, her work has been featured on Gently Radiant, Morning Vessels, and Hymn & Tea Journal (Fall 2011).

Lorena ‘s first book, Leaving the Lantern Hall: Revealing Hidden Snares in Ordinary Routines, is an informative memoir and Bible study, recounting her journey from committed Christian to witch, medium, and ghost hunter for eight years until restored to faith in Jesus Christ. She was a contributing author to Walking the Shadow Road: A Plain Account of Dark Arts from Past Seekers by Dale Winterbottom and a consultant for the novel The Keeper of Pellam Hollow by Lumen Prize Winning Author, Norma Quillfeather.

Lorena’s second book, An Insider’s Guide to Spiritual Warfare: 20 Battle-Tested Strategies from Behind Enemy Lines, will be published by Ridgeway Press for Fall 2014.

Lorena is a wife and mother. She enjoys writing, spending time with her family, taking long walks, listening to music of all kinds, and experiencing God’s daily gift called life.

You can read more about Lorena and see the look and feel we are going for at www.lorenawatkiss.example

The brochure is to be used as a promotional tool to gain Lorena speaking engagements. You can see the topics she covers at http://www.lorenawatkiss.example/speaking-engagements/.

More info can be found at: https://www.social.example/AuthorLorenaWatkiss
https://www.social.example/VMUCX
https://www.social.example/LeavingtheLanternHall
https://www.social.example/TallOakOutreach
http://www.talloakoutreach.example

I have uploaded 3 headshots, book covers for both of Lorena's books and the design layout in .EPS format from Quickprintly.example where I will be getting printing done.

3 more days till the contest ends get your final designs in.

Reason: I'm extending this as I am tied up at a leadership conference and will not be able to give this the attention it deserves till the weekend.

Target Market(s)

Churches and women's groups. Lorena's current audience skews heavy to women on a 70/30 ratio.

Industry/Entity Type

Christian

Requirements
Must have
• Headshot I have uploaded 3
Quotes from previous speaking engagements you can find those at http://www.lorenawatkiss.example/speaking-engagements/

```html
<!DOCTYPE html>
<html lang="en">
<head>
<meta charset="utf-8">
<title>Lorena Watkiss — Author | Speaker</title>
<link rel="stylesheet" href="https://fonts.googleapis.com/css2?family=Cinzel:wght@400;500&family=Libre+Baskerville:ital,wght@0,700;1,400&family=Arimo:wght@700&display=swap">
<style>
  :root{
    --maroon:#5e1018;
    --title:#6d1b26;
    --ink:#2a1e20;
    --blossom-light:#fbeef2;
    --blossom-mid:#f1cdd8;
    --blossom-deep:#dca2b5;
    --white:#ffffff;
  }
  *{box-sizing:border-box;margin:0;padding:0}
  html,body{width:1200px;height:848px;overflow:hidden}
  body{background:var(--blossom-light);position:relative;font-family:"Libre Baskerville",Georgia,serif;color:var(--ink)}

  .backdrop{position:absolute;inset:0;
    background:
      radial-gradient(ellipse 420px 300px at 260px 60px,var(--blossom-deep),transparent 70%),
      radial-gradient(ellipse 380px 260px at 1080px 90px,var(--blossom-mid),transparent 70%),
      radial-gradient(ellipse 520px 360px at 640px 760px,var(--blossom-mid),transparent 70%),
      linear-gradient(160deg,#f7dde5 0%,var(--blossom-light) 45%,#f6e2e8 100%);}

  .portrait{position:absolute;background:linear-gradient(160deg,#8a5a4e,#c99a8c 55%,#e7c9c6);}
  .portrait--header{left:0;top:0;width:103px;height:135px}
  .portrait--feature{left:0;top:143px;width:150px;height:263px;background:linear-gradient(170deg,#6f5a58,#3a2c2c 60%,#c7a9a3)}

  .masthead__name,.masthead__role{position:absolute;font-family:"Cinzel",serif;font-weight:400;color:var(--title);white-space:nowrap;line-height:1;letter-spacing:1px}
  .masthead__name{left:111px;top:76px;font-size:60px}
  .masthead__role{left:770px;top:92px;font-size:40px}

  .intro{position:absolute;left:156px;top:160px;width:212px;font-style:italic;font-size:13.6px;line-height:18.5px}
  .intro::before{content:"";float:left;width:0;height:56px}
  .intro__indent{float:left;clear:left;width:48px;height:150px}

  .quote-bar{position:absolute;left:0;top:408px;width:382px;height:48px;background:var(--maroon);
    color:var(--white);font-family:"Arimo",Arial,sans-serif;font-weight:700;font-size:20px;
    display:flex;align-items:center;padding-left:36px}

  .column{position:absolute;overflow:hidden;font-size:13.6px;line-height:19.5px}
  .column--left{left:36px;top:470px;width:340px;height:376px}
  .column--middle{left:416px;top:160px;width:386px;height:686px}
  .column--right{left:819px;top:148px;width:372px;height:698px}

  .column--middle::before{content:"";float:right;width:0;height:248px}
  .column--middle .topics-gap{float:right;clear:right;width:150px;height:284px}
  .column--right::before{content:"";float:left;width:0;height:262px}
  .column--right .topics-gap{float:left;clear:left;width:46px;height:282px}

  .testimonial__source{font-weight:700;font-size:14.5px;line-height:19px;margin-bottom:5px}
  .testimonial__text{font-style:italic}
  .testimonial+.testimonial,.column--right .testimonial{margin-top:18px}

  .topics{position:absolute;left:663px;top:412px;width:192px;height:266px;background:var(--maroon);
    color:var(--white);font-family:"Arimo",Arial,sans-serif;text-align:center;padding-top:14px}
  .topics__title{font-size:18px;font-weight:700;margin-bottom:14px}
  .topics__list{list-style:none;font-family:Arial,Helvetica,sans-serif;font-size:12.5px;line-height:16px}
  .topics__list li{margin-bottom:17px}
</style>
</head>
<body>
  <div class="backdrop" role="img" aria-label="Soft pink cherry blossom background"></div>

  <div class="portrait portrait--header" role="img" aria-label="Headshot of Lorena Watkiss"></div>
  <header class="masthead">
    <h1 class="masthead__name">Lorena Watkiss</h1>
    <span class="masthead__role">Author | Speaker</span>
  </header>

  <div class="portrait portrait--feature" role="img" aria-label="Photo of Lorena Watkiss speaking at an event"></div>
  <p class="intro"><span class="intro__indent"></span>As a speaker, Lorena Watkiss shares from her own life lessons and as a Biblical Counselor, encouraging others toward a deeper walk with God. Lorena offers sound, heartfelt, and practical biblical advice on issues relevant to the 21st Century Christian</p>

  <div class="quote-bar">Lorena Like As A Speaker?</div>

  <section class="column column--left">
    <article class="testimonial">
      <h2 class="testimonial__source">Linnea Braddock, Clearwater Community Church Women’s Ministry:</h2>
      <p class="testimonial__text">The Women’s Ministry at Clearwater Church in Maple Ridge, MI invited Lorena Watkiss to speak at our Mother or Daughter Banquet earlier this month. I am so glad she accepted! We couldn’t have chosen a speaker to fit in better than Lorena. She took our theme, “Instruments”, and incorporated that into her speaking time with us. She used life examples and spoke directly into the hearts of the women and girls that attended our banquet. She even took time to speak to my teen aged daughters after the banquet as to why they should stay away from the paranormal. I highly recommend Lorena as a speaker and we hope to have her back at Clearwater Church in the near future!</p>
    </article>
  </section>

  <section class="column column--middle">
    <div class="topics-gap"></div>
    <article class="testimonial">
      <h2 class="testimonial__source">Mae Dellinger, Hymn and Tea Women’s Ministry Events:</h2>
      <p class="testimonial__text">“Lorena came to our Hymn and Tea Night and shared her story, it was amazing! I’ve never seen women so riveted by a speaker! If you are in a position to bring Lorena to your church/event…do it!”</p>
    </article>
    <article class="testimonial">
      <h2 class="testimonial__source">Gavin Ostrander, Kinship Crossroads Seminar Tent, Coordinator:</h2>
      <p class="testimonial__text">“I was honored and delighted to have Lorena Watkiss be one of our speakers in the “Kinship Crossroads Seminar Tent” at Kinship Christian Music Festival in Harlow Bay, Michigan (one of the nation’s top 10 Christian music festivals). Lorena has a unique testimony and style of speaking that keeps people, young and old, engaged into the heart of her message. Her stories of involvement in the occult and her conclusion of how God rescued her from these traps, answers many of the questions that people often have, but are afraid to ask when dealing with the “supernatural”. If you are looking for a great speaker with a testimony that is relevant in today’s culture of “curiosity in the supernatural”, I highly recommend Lorena Watkiss to be on the top of your list of considerations.”</p>
    </article>
    <article class="testimonial">
      <h2 class="testimonial__source">Ruth Ellington, Hope Harbor Church, Women’s Christmas Tea Coordinator:</h2>
      <p class="testimonial__text">“We had Lorena speak at our Women’s Tea. Even though the weather was terrible in Northern Michigan we had a good turnout and I</p>
    </article>
  </section>

  <aside class="topics">
    <h2 class="topics__title">Speaking Topics</h2>
    <ul class="topics__list">
      <li>Christians and the Occult</li>
      <li>Homelessness<br>(with Dean Watkiss)</li>
      <li>Human Trafficking</li>
      <li>Marriage Restoration<br>(with Dean Watkiss)</li>
      <li>Prayer as a Lifestyle</li>
      <li>Spiritual Warfare</li>
    </ul>
  </aside>

  <section class="column column--right">
    <div class="topics-gap"></div>
    <p class="testimonial__text">had several women tell me afterwards how blessed they were with Lorena’s message. The emphasis was on putting Christ first during the holidays and not getting so busy we forget what Christmas is really about. Lorena was an enthusiastic and wonderful from-the-heart speaker. We hope to have her back again!”</p>
    <article class="testimonial">
      <h2 class="testimonial__source">Rob Vanterpool, Pastor, Stonegate Reformed Church:</h2>
      <p class="testimonial__text">“Lorena Watkiss spoke at our church sharing with us her testimony which includes how she attempted to blend witchcraft with Christianity. Obviously, she discovered that there is no compromising of the Gospel and the Holy Spirit brought her back in an amazing way. Her story is gripping. It also serves as a warning to not blend religion “ala carte” and to pay close attention to the Word of God. Lorena notes well that we all have a spiritual hunger, and if we don’t satisfy it with Christ and His word, we may slip into any kind of spiritual offering. The church needs to hear her story. It is a wake up call to be aware of the continual influence of our culture pushing us into consideration of the paranormal and other strange spiritual activity. It is also a pointed reminder that we, the church, need to be on the offensive knowing what we believe and to be willing to share it with searching, hungry souls. Lorena rounds out her story with sound theology and giving praise and glory to God. I would highly recommend to you that you engage Lorena in speaking to your church groups.”</p>
    </article>
  </section>
</body>
</html>
```